Stationery and Business Card Design

We need stationary design for our new company pelvanta. Pelvanta is a company that provides city apartment rentals for tourists in Athens We need business cards, letterheads for A4 and A5 and envelopes for A4 A5. The design needs to be modern, friendly and corporate.

Target Market(s)

City Tourists

Industry/Entity Type

Tourism

```html
<!DOCTYPE html>
<html lang="en">
<head>
<meta charset="utf-8">
<title>Pelvanta Envelope</title>
<link href="https://fonts.googleapis.com/css2?family=Raleway:wght@500&family=Michroma&display=swap" rel="stylesheet">
<style>
  :root {
    --brand: #8e0055;
    --paper: #e6e6e8;
    --mark-faint: #dcc4d1;
    --rule: #a8a8ab;
    --stage-light: #ffffff;
    --stage-dark: #2b2b2c;
    --shadow: rgba(0, 0, 0, 0.55);
  }
  * { margin: 0; padding: 0; box-sizing: border-box; }
  html, body { width: 1200px; height: 900px; overflow: hidden; }
  body { position: relative; background: var(--stage-light); font-family: "Raleway", sans-serif; }

  .stage { position: absolute; left: 0; width: 1200px; }
  .stage--light { top: 0; height: 530px; background: var(--stage-light); }
  .stage--dark { top: 530px; height: 370px; background: var(--stage-dark); }

  .envelope {
    position: absolute;
    left: 189px;
    width: 846px;
    height: 300px;
    background: var(--paper);
    box-shadow: 5px 6px 5px var(--shadow);
  }
  .stage--light .envelope { top: 128px; }
  .stage--dark .envelope { top: 35px; }

  .envelope__band {
    position: absolute; top: 0; bottom: 0; background: var(--brand);
  }
  .envelope__band--left { left: 0; width: 27px; }
  .envelope__band--right { right: 0; width: 30px; }

  .envelope__corner-block {
    position: absolute; top: 4px; right: 30px;
    width: 126px; height: 124px;
    background: var(--mark-faint);
  }

  .brand {
    position: absolute; left: 54px; top: 27px; width: 150px;
    display: flex; flex-direction: column; align-items: center;
  }
  .brand__square { width: 44px; height: 40px; background: var(--brand); }
  .brand__name {
    margin-top: 7px;
    font-size: 33px; font-weight: 500; line-height: 1;
    color: var(--brand); letter-spacing: -0.5px;
  }
  .brand__tag {
    display: flex; align-items: center; gap: 6px; margin-top: 2px;
    font-size: 7px; letter-spacing: 2px; color: var(--brand);
    font-family: "Michroma", sans-serif;
  }
  .brand__tag::before, .brand__tag::after {
    content: ""; width: 22px; height: 2px; background: var(--rule);
  }

  .envelope__sender {
    position: absolute; right: 52px; bottom: 22px;
    font-family: "Michroma", sans-serif;
    font-size: 17px; letter-spacing: 3px;
    color: var(--brand);
  }
</style>
</head>
<body>
  <section class="stage stage--light">
    <div class="envelope">
      <div class="envelope__band envelope__band--left"></div>
      <div class="envelope__band envelope__band--right"></div>
      <div class="envelope__corner-block"></div>
      <div class="brand">
        <div class="brand__square"></div>
        <div class="brand__name">Pelvanta</div>
        <div class="brand__tag">APARTMENTS</div>
      </div>
      <p class="envelope__sender">PELVANTA APARTMENT</p>
    </div>
  </section>

  <section class="stage stage--dark">
    <div class="envelope">
      <div class="envelope__band envelope__band--left"></div>
      <div class="envelope__band envelope__band--right"></div>
      <div class="envelope__corner-block"></div>
      <div class="brand">
        <div class="brand__square"></div>
        <div class="brand__name">Pelvanta</div>
        <div class="brand__tag">APARTMENTS</div>
      </div>
      <p class="envelope__sender">PELVANTA APARTMENT</p>
    </div>
  </section>
</body>
</html>
```